The Pixel Tap Business card.

A Simple card with our Logo and contact information. To give to investors and other professionals.

We are a nerd themed bar.
our target market is young professionals age 21+ but the real purpose of this business card is to present to potential investors and other professionals with our contact information. as we are still looking for funding before we start up.

I am partial to green and my partner likes red we are open to iteration.

Target Market(s)

Investors

Industry/Entity Type

Business

Contact Information for Business Card

Martin Hale (225) 730-6192 kent.h4711@mailnest.test Glen Porter (225) 968-5037 glenp318@mailnest.test

Font styles to use
Serif

Requirements
Nice to have
• Keep it simple but not boring.
• Use the Logos but feel free to edit them to match theme/colors.
• Keep the back clean and use one of the Logos.

```html
<!DOCTYPE html>
<html lang="en">
<head>
<meta charset="UTF-8">
<title>The Pixel Tap — Business Card</title>
<link rel="stylesheet" href="https://fonts.googleapis.com/css2?family=Roboto:wght@400;700;900&display=swap">
<style>
  :root {
    --stage: #e9e6e1;
    --brand-red: #e61b2b;
    --ink: #111111;
    --paper: #ffffff;
    --band: #0b0b0b;
    --band-text: #f2f2f2;
    --rule: #bdbdbd;
  }
  * { box-sizing: border-box; margin: 0; padding: 0; }
  html, body { width: 1200px; height: 950px; overflow: hidden; }
  body {
    background: var(--stage);
    font-family: "Roboto", Arial, sans-serif;
    display: flex;
    flex-direction: column;
    align-items: center;
    justify-content: center;
    gap: 70px;
  }
  .card {
    width: 580px;
    height: 330px;
    position: relative;
    overflow: hidden;
    box-shadow: 0 10px 24px rgba(0,0,0,0.22);
  }
  .card-back {
    background: var(--brand-red);
    display: flex;
    align-items: center;
    justify-content: center;
  }
  .wordmark {
    display: flex;
    align-items: center;
    gap: 14px;
    font-weight: 900;
    font-size: 40px;
    letter-spacing: 1px;
    text-transform: uppercase;
    color: var(--ink);
  }
  .wordmark-dot {
    width: 22px;
    height: 22px;
    border-radius: 50%;
    background: var(--ink);
  }
  .card-front { background: var(--paper); }
  .card-front .logo-area {
    height: 210px;
    display: flex;
    align-items: center;
    justify-content: center;
  }
  .card-front .wordmark-dot { background: var(--brand-red); }
  .contact-band {
    position: absolute;
    left: 0; right: 0; bottom: 0;
    height: 120px;
    background: linear-gradient(180deg, #1c1c1c 0%, var(--band) 60%);
    color: var(--band-text);
  }
  .band-edge {
    position: absolute;
    top: 0; left: 0;
    width: 100%;
    height: 10px;
  }
  .contact-name {
    position: absolute;
    top: 24px; left: 0; right: 0;
    display: flex;
    align-items: center;
    justify-content: center;
    gap: 14px;
    font-size: 19px;
    font-weight: 700;
  }
  .contact-name::before,
  .contact-name::after {
    content: "";
    width: 120px;
    height: 1px;
    background: var(--rule);
  }
  .contact-lines {
    position: absolute;
    top: 62px; left: 0; right: 0;
    display: flex;
    justify-content: center;
    gap: 22px;
    font-size: 15px;
  }
  .contact-item { display: flex; align-items: center; gap: 7px; }
  .contact-item svg { fill: var(--band-text); }
</style>
</head>
<body>
  <section class="card card-back" aria-label="Card back">
    <div class="wordmark"><span class="wordmark-dot"></span><span>The Pixel Tap</span></div>
  </section>

  <section class="card card-front" aria-label="Card front">
    <div class="logo-area">
      <div class="wordmark"><span class="wordmark-dot"></span><span>The Pixel Tap</span></div>
    </div>
    <div class="contact-band">
      <svg class="band-edge" viewBox="0 0 580 10" preserveAspectRatio="none" aria-hidden="true">
        <line x1="0" y1="2" x2="580" y2="2" stroke="#ffffff" stroke-width="2"/>
        <g stroke="#ffffff" stroke-width="2">
          <line x1="58" y1="2" x2="58" y2="9"/>
          <line x1="116" y1="2" x2="116" y2="9"/>
          <line x1="174" y1="2" x2="174" y2="9"/>
          <line x1="232" y1="2" x2="232" y2="9"/>
          <line x1="290" y1="2" x2="290" y2="9"/>
          <line x1="348" y1="2" x2="348" y2="9"/>
          <line x1="406" y1="2" x2="406" y2="9"/>
          <line x1="464" y1="2" x2="464" y2="9"/>
          <line x1="522" y1="2" x2="522" y2="9"/>
        </g>
      </svg>
      <div class="contact-name">Martin Hale</div>
      <div class="contact-lines">
        <span class="contact-item">
          <svg width="11" height="17" viewBox="0 0 11 17" aria-hidden="true"><path d="M1.5 0h8A1.5 1.5 0 0 1 11 1.5v14A1.5 1.5 0 0 1 9.5 17h-8A1.5 1.5 0 0 1 0 15.5v-14A1.5 1.5 0 0 1 1.5 0zM1.5 2v11h8V2zM5.5 14a.9.9 0 1 0 0 1.8.9.9 0 0 0 0-1.8z"/></svg>
          (225) 730-6192
        </span>
        <span class="contact-item">
          <svg width="16" height="11" viewBox="0 0 16 11" aria-hidden="true"><path d="M0 0h16v11H0zM1 1v.4l7 5 7-5V1zm0 1.6V10h14V2.6L8 7.6z"/></svg>
          kent.h4711@mailnest.test
        </span>
      </div>
    </div>
  </section>
</body>
</html>
```